Postcard Mailer

We are a pizza pub that is the only local restaurant that offers and delivers pizza, burgers, salads and wings.

We just opened and want to send out a postcard to the community. thinking on one side a nice design with pics etc. then on the back a list of our daily food and drink specials.

Industry/Entity Type

Restaurant

Colors
eb1f27

```html
<!DOCTYPE html>
<html lang="en">
<head>
<meta charset="utf-8">
<title>Pizza Pub Postcard – Menu Side</title>
<link rel="stylesheet" href="https://fonts.googleapis.com/css2?family=Yellowtail&family=Oswald:wght@600;700&family=Open+Sans:ital,wght@0,400;1,700&display=swap">
<style>
  :root {
    --red: #eb1f27;
    --red-deep: #7e0a12;
    --gold: #c9892f;
    --white: #ffffff;
    --ink: #111111;
    --line: #c98a8a;
    --stamp: #8e2a2a;
    --edge: #bdbdbd;
  }
  * { box-sizing: border-box; margin: 0; padding: 0; }
  html, body { width: 1200px; height: 840px; overflow: hidden; background: var(--white); }
  .postcard { position: relative; width: 1200px; height: 840px; background: var(--white); }

  .menu-panel {
    position: absolute; left: 0; top: 0; width: 612px; height: 840px;
    background: linear-gradient(180deg, var(--red) 0%, #c8141c 55%, var(--red-deep) 100%);
  }
  .menu-title {
    position: absolute; left: 96px; top: 14px;
    font-family: "Yellowtail", cursive; font-size: 48px; color: var(--white); font-weight: 400;
  }
  .special {
    position: absolute; left: 43px;
    font-family: "Open Sans", sans-serif; color: var(--white);
    font-size: 17.5px; line-height: 21.6px;
  }
  .special-day { font-weight: 700; font-style: italic; font-size: 18.5px; line-height: 23px; }

  .price-badge {
    position: absolute; left: 352px; width: 260px; height: 142px;
    border: 9px solid var(--gold); border-radius: 26px;
    background: var(--white);
    box-shadow: inset 0 0 0 5px var(--red);
    display: flex; align-items: center; justify-content: center; text-align: center;
    font-family: "Oswald", sans-serif; font-weight: 700; color: var(--ink);
    font-size: 35px; line-height: 1.12; letter-spacing: -0.2px;
  }
  .price-badge.tight { font-size: 31px; line-height: 1.2; }

  .mail-side {
    position: absolute; left: 612px; top: 0; width: 588px; height: 840px;
    border-left: 2px solid var(--edge); border-top: 1px solid var(--edge);
  }
  .stamp-box {
    position: absolute; left: 1014px; top: 26px; width: 165px; height: 221px;
    border: 3px solid var(--stamp); border-radius: 4px;
  }
  .address-line {
    position: absolute; left: 667px; width: 515px; height: 0;
    border-top: 2px dashed var(--line);
  }
</style>
</head>
<body>
<div class="postcard">
  <section class="menu-panel">
    <h1 class="menu-title">Our Menu</h1>

    <div class="special" style="top:94px"><p class="special-day">Daily Lunch Special</p><p>2 Slices + Drink $4.95</p></div>
    <div class="special" style="top:164px"><p class="special-day">Monday</p><p>Buy 1 Medium Pizza Get 1 Free</p><p>$1 Domestic Beers</p></div>
    <div class="special" style="top:256px"><p class="special-day">Tuesday</p><p>Medium Pizza $7.95</p><p>50 cent wings</p><p>$1.50 Drafts</p></div>
    <div class="special" style="top:369px"><p class="special-day">Wednesday</p><p>Classic Burger + Beer $5.95</p><p>$2.50 Ember Shots</p></div>
    <div class="special" style="top:460px"><p class="special-day">Thursday</p><p>$1 Slice Night</p><p>$2.50 Craft Beers</p></div>
    <div class="special" style="top:552px"><p class="special-day">Friday</p><p>2 Medium Pizzas $15.95</p><p>$2 Glasses of Wine</p></div>
    <div class="special" style="top:645px"><p class="special-day">Saturday</p><p>1/2 Price Salads</p><p>$3 Vodka Drinks</p><p>$2.50 Harbor Twin Ale</p></div>
    <div class="special" style="top:758px"><p class="special-day">Sunday</p><p>Large Pizza $9.95</p><p>$3 Bloody Mary's &amp; Mimosa's</p></div>

    <div class="price-badge" style="top:20px">By The Slice<br>$2</div>
    <div class="price-badge" style="top:188px">Medium 14”<br>Pie $11.95</div>
    <div class="price-badge" style="top:353px">Large 16”<br>Pie $13.95</div>
    <div class="price-badge tight" style="top:518px">Speciality Pizzas<br>Medium 14”<br>$13.95</div>
    <div class="price-badge tight" style="top:680px">Speciality Pizzas<br>Large 16”<br>$18.95</div>
  </section>

  <section class="mail-side" aria-label="Mailing side"></section>
  <div class="stamp-box" aria-label="Stamp area"></div>
  <div class="address-line" style="top:491px"></div>
  <div class="address-line" style="top:551px"></div>
  <div class="address-line" style="top:613px"></div>
  <div class="address-line" style="top:673px"></div>
  <div class="address-line" style="top:735px"></div>
</div>
</body>
</html>
```